one pager for investors

I will give an initial file in any format needed. Also, the photo that must be included. As well as the logo, that must be the key to the overall design in terms of font, colors, and general layout. I will attach a file in PDF format, which is a one pager presenting a project for investors that I would like to attract and convinced to invest in my project. What I would like you to do is propose me different and better design options, taking my first draft as an example. But you must absolutely keep every single word and number, absolutely all the information written in my first draft(except “ TEMPLATE DRAFT”). Also, on the top left corner is the logo of our company, which I think should be your main inspiration document is a one pager presented to potential investors that not only has to include the most important information in order for them to be able to see everything needed to see the value of the project (which I’ve already taken care of by writing the text needed, numbers presented and timeline shown; all of which which must be preserved in terms of content, but can be completely redesigned and manipulated ) sh a.k.a. Project summary for investor to go for it.
Target Market(s)
Serious rich investors
Industry/Entity Type
Real eatate

```html
<!DOCTYPE html>
<html lang="fr">
<head>
<meta charset="utf-8">
<title>Veranor Properties SA – Description du projet</title>
<link href="https://fonts.googleapis.com/css2?family=Archivo:wght@400;500;700;800&display=swap" rel="stylesheet">
<style>
  :root {
    --brand-blue: #3d55a5;
    --ink: #1d1d22;
    --ink-soft: #3a3a44;
    --card-grey: #ededf0;
    --card-blue: #e6e9f3;
    --line-blue: #7a9cc8;
    --paper: #ffffff;
  }
  * { box-sizing: border-box; margin: 0; padding: 0; }
  html, body { width: 960px; height: 1200px; overflow: hidden; background: var(--paper); }
  body { font-family: "Archivo", Arial, sans-serif; color: var(--ink); }

  .page { position: relative; width: 960px; height: 1200px; overflow: hidden; background: var(--paper); }

  .hero-photo {
    position: absolute; left: 0; top: 0; width: 960px; height: 520px;
    background:
      linear-gradient(180deg, rgba(255,255,255,0) 60%, rgba(255,255,255,0.25) 100%),
      linear-gradient(120deg, #d9dde4 0%, #c9ccd2 28%, #9a7a62 48%, #6b5448 62%, #8a8f7a 78%, #b86a3a 100%);
  }

  .brand-panel {
    position: absolute; left: 0; top: 340px; width: 470px; height: 110px;
    background: rgba(255, 255, 255, 0.85);
    display: flex; align-items: center; gap: 18px; padding-left: 50px;
  }
  .brand-dot { width: 22px; height: 22px; border-radius: 50%; background: var(--ink); flex: none; }
  .brand-name { font-size: 34px; font-weight: 500; color: var(--ink); line-height: 1; }

  .intro-frame {
    position: absolute; left: 60px; top: 520px; width: 840px; height: 220px;
    border: 2px solid var(--brand-blue);
  }
  .title-band {
    position: absolute; left: 0; top: 470px; width: 960px; height: 90px;
    background: var(--brand-blue);
  }
  .title-band h1 {
    position: absolute; left: 290px; top: 18px;
    font-size: 46px; font-weight: 800; color: #fff; letter-spacing: 0.5px;
  }

  .intro {
    position: absolute; left: 100px; top: 585px; width: 760px;
    text-align: center; font-size: 17px; line-height: 1.45; color: var(--ink);
  }
  .duration { display: block; margin-top: 10px; }

  .card { position: absolute; border-radius: 0 0 4px 4px; }
  .card-tab {
    height: 62px; border-radius: 36px 36px 0 0;
    display: flex; align-items: center; justify-content: center; text-align: center;
    color: #fff; font-weight: 800; font-size: 19px; line-height: 1.1; letter-spacing: 0.3px;
  }
  .finance { left: 140px; top: 762px; width: 360px; height: 290px; background: var(--card-grey); }
  .finance .card-tab { background: var(--ink); }
  .structure { left: 530px; top: 762px; width: 340px; height: 272px; background: var(--card-blue); }
  .structure .card-tab { background: var(--brand-blue); height: 76px; }

  .figures { list-style: none; padding: 14px 22px 0; font-size: 14px; }
  .figures li { display: flex; justify-content: space-between; line-height: 1.35; color: var(--ink-soft); }
  .figures li.gap { margin-top: 10px; }
  .figures li.key { font-weight: 700; color: var(--ink); }
  .figures .value { white-space: nowrap; }

  .timeline { position: absolute; left: 0; top: 1040px; width: 960px; height: 110px; }
  .timeline text { font-family: "Archivo", Arial, sans-serif; font-size: 14px; fill: var(--ink-soft); }

  .footer-band {
    position: absolute; left: 0; bottom: 0; width: 960px; height: 52px;
    background: var(--brand-blue); color: #fff;
    display: flex; align-items: center; justify-content: space-between;
    padding: 0 60px; font-size: 14px;
  }
</style>
</head>
<body>
<main class="page">
  <div class="hero-photo" role="img" aria-label="Photo of a modern three-storey residential building with balconies and autumn trees"></div>

  <div class="brand-panel">
    <span class="brand-dot"></span>
    <span class="brand-name">Veranor Properties SA</span>
  </div>

  <div class="intro-frame"></div>
  <div class="title-band"><h1>Description Du Projet</h1></div>

  <p class="intro">
    Le projet XXX est un projet de développement de 30 appartements de standing en PPE au centre de Lausanne. Le terrain a été sécurisé par la signature du vente à terme conditionnelle. L'objectif est d'obtenir le permis de construire, puis de vendre les lots. Dans un premier temps sur plan puis au fil de la construction.
    <span class="duration">Durée estimée du projet – 24 à 36 mois.</span>
  </p>

  <section class="card finance">
    <h2 class="card-tab">PLAN FINANCIER</h2>
    <ul class="figures">
      <li><span>Prix du terrain</span><span class="value">CHF 2'000'000</span></li>
      <li><span>Frais d'acquisition</span><span class="value">CHF 100'000</span></li>
      <li class="gap"><span>Coût de construction</span><span class="value">CHF 2'500'000</span></li>
      <li><span>Divers &amp; imprévus</span><span class="value">CHF 200'000</span></li>
      <li class="key"><span>Prix de revient total</span><span class="value">CHF 4'800'000</span></li>
      <li class="gap key"><span>Prix de vente total</span><span class="value">CHF 7'500'000</span></li>
      <li><span>Honoraires sur vente</span><span class="value">CHF 190'000</span></li>
      <li class="gap key"><span>Marge projet</span><span class="value">CHF 2'510'000</span></li>
      <li class="key"><span>En % sur prix de vente</span><span class="value">33.47%</span></li>
    </ul>
  </section>

  <section class="card structure">
    <h2 class="card-tab">STRUCTURE<br>D'INVESTISSEMENT</h2>
    <ul class="figures">
      <li><span>Besoin de fonds propres</span><span class="value">CHF 2'000'000</span></li>
      <li><span>Retour de fonds total</span><span class="value">CHF 3'156'600</span></li>
      <li class="gap key"><span>Bénéfice net investisseur</span><span class="value">CHF 1'656'600</span></li>
      <li><span>Soit 2/3 du bénéfice projet</span><span></span></li>
      <li class="gap key"><span>Multiple sur fonds propres</span><span class="value">x1.58</span></li>
      <li class="gap key"><span>Rendement annualisé</span><span class="value">41.4%</span></li>
      <li><span>Calcul sur 24 mois</span><span></span></li>
    </ul>
  </section>

  <svg class="timeline" viewBox="0 0 960 110" aria-label="Calendrier du projet">
    <line x1="110" y1="50" x2="880" y2="50" stroke="var(--line-blue)" stroke-width="4"/>
    <polygon points="880,38 906,50 880,62" fill="var(--line-blue)"/>
    <g stroke="var(--line-blue)" stroke-width="2">
      <line x1="190" y1="38" x2="190" y2="62"/>
      <line x1="390" y1="38" x2="390" y2="62"/>
      <line x1="590" y1="38" x2="590" y2="62"/>
      <line x1="790" y1="38" x2="790" y2="62"/>
    </g>
    <g text-anchor="middle">
      <text x="190" y="28">08.2024</text>
      <text x="390" y="28">04.2025</text>
      <text x="590" y="28">12.2025</text>
      <text x="790" y="28">12.2026</text>
      <text x="190" y="82">Achat parcelle</text>
      <text x="390" y="82">Mise à l'enquête</text>
      <text x="590" y="82">Début construction</text>
      <text x="790" y="82">Livraison</text>
    </g>
  </svg>

  <footer class="footer-band">
    <span>Veranor Properties Vaud SA - Chemin des Vergers 8 - CH-1100 Morval</span>
    <span>Page 1/2</span>
  </footer>
</main>
</body>
</html>
```